Business cards and stationary
IT Consultancy
Professional
Dermot Ashby
Managing Director
27 Larch Chambers
62 Pellbrook Gardens
Ashmere
Hollbury
TW3 5RJ
dermot.ashby@brevix.com
www.brevix.com
Would like to incorporate both types of logos (white on black and black on white)
Also, like an A4 folder design to house brochures.

```html
<!DOCTYPE html>
<html lang="en">
<head>
<meta charset="utf-8">
<title>Brevix Stationery Set</title>
<link rel="stylesheet" href="https://fonts.googleapis.com/css2?family=Arimo:wght@400;700&display=swap">
<style>
:root{
  --navy:#1c3f86;
  --blue-deep:#123a8a;
  --blue-light:#3f8fdc;
  --red:#d2232a;
  --ink:#333;
  --grey:#7a7a7a;
  --paper:#fff;
  --edge:#d9d9d9;
  --faint:#eef1f6;
}
*{box-sizing:border-box;margin:0;padding:0}
html,body{width:1200px;height:754px;overflow:hidden;background:#fff;font-family:"Arimo",Arial,sans-serif;color:var(--ink)}
.canvas{position:relative;width:1200px;height:754px}
.sheet{position:absolute;background:var(--paper);border:1px solid var(--edge);box-shadow:1px 1px 3px rgba(0,0,0,.18);overflow:hidden}

/* wordmark */
.brand{display:flex;align-items:center;gap:6px}
.brand-dot{border-radius:50%;background:var(--red);flex:none}
.brand-name{font-weight:700;color:var(--navy);letter-spacing:.04em;line-height:1}
.brand-sub{font-size:6px;color:var(--navy);letter-spacing:.02em;margin-top:2px;white-space:nowrap}
.brand-tag{font-size:6px;color:var(--grey);letter-spacing:.25em;text-transform:uppercase;margin-top:2px;white-space:nowrap}

/* letterhead */
.letterhead{left:43px;top:12px;width:514px;height:727px}
.letterhead .brand{position:absolute;left:12px;top:14px}
.letterhead .brand-dot{width:26px;height:26px}
.letterhead .brand-name{font-size:34px}
.letterhead .brand-sub{font-size:6.5px}
.letterhead .brand-tag{font-size:7px}
.watermark{position:absolute;left:95px;top:150px;width:330px;height:330px;border-radius:50%;background:var(--faint);display:flex;align-items:center;justify-content:center}
.watermark span{font-weight:700;font-size:64px;color:#e2e7f0;letter-spacing:.04em}
.letter-foot{position:absolute;left:12px;top:646px;font-size:10px;line-height:13px}
.letter-foot .label{color:var(--red)}
.letter-foot .web{color:var(--red)}

/* business card */
.card-front{left:569px;top:12px;width:276px;height:132px}
.card-band{position:absolute;left:0;top:0;width:100%;height:16px;background:linear-gradient(90deg,var(--blue-deep),var(--blue-light))}
.card-front .brand{position:absolute;left:8px;top:22px;gap:4px}
.card-front .brand-dot{width:12px;height:12px}
.card-front .brand-name{font-size:17px}
.card-front .brand-sub{font-size:3.5px}
.card-front .brand-tag{font-size:3.5px}
.card-person{position:absolute;left:150px;top:56px;font-size:7px;line-height:9px}
.card-person .role{color:var(--red);font-size:5.5px}
.card-address{position:absolute;left:10px;top:86px;font-size:5px;line-height:6.5px}
.card-address .label{color:var(--red)}
.card-faint{position:absolute;right:12px;bottom:8px;width:40px;height:40px;border-radius:50%;background:var(--faint)}

/* logo cards */
.card-logo{display:flex;align-items:center;justify-content:center;border:none}
.card-blue{left:636px;top:168px;width:180px;height:101px;background:radial-gradient(ellipse at 60% 45%,var(--blue-light),var(--blue-deep) 75%)}
.card-black{left:874px;top:233px;width:182px;height:96px;background:#0d0d10}
.card-logo .brand-dot{width:14px;height:14px}
.card-logo .brand-name{font-size:26px;color:#fff}
.card-logo .brand-sub,.card-logo .brand-tag{color:#dfe6f2;font-size:4px}

/* envelope */
.envelope{left:569px;top:384px;width:607px;height:360px}
.envelope svg.flap{position:absolute;left:0;top:0}
.flap-mark{position:absolute;left:291px;top:24px;width:24px;height:24px;border-radius:50%;background:var(--red)}
.envelope .brand{position:absolute;left:12px;top:150px}
.envelope .brand-dot{width:26px;height:26px}
.envelope .brand-name{font-size:36px}
.envelope .brand-sub{font-size:6.5px}
.envelope .brand-tag{font-size:7px}
.env-address{position:absolute;left:43px;top:262px;font-size:10px;line-height:12.5px}
.env-faint{position:absolute;right:24px;bottom:16px;width:80px;height:80px;border-radius:50%;background:var(--faint)}
</style>
</head>
<body>
<main class="canvas">

  <section class="sheet letterhead" aria-label="Letterhead">
    <div class="brand">
      <span class="brand-dot"></span>
      <div>
        <div class="brand-name">BREVIX</div>
        <div class="brand-sub">Brevix Systems Group</div>
        <div class="brand-tag">Strategic Consulting</div>
      </div>
    </div>
    <div class="watermark" aria-hidden="true"><span>BREVIX</span></div>
    <div class="letter-foot">
      <p>27 Larch Chambers, 62 Pellbrook Gardens, Ashmere, Hollbury. TW3 5RJ</p>
      <p><span class="label">Phone:</span> 01632 960 418 <span class="label">| Cell:</span> 07700 900 612</p>
      <p class="web">www.brevix.com</p>
    </div>
  </section>

  <section class="sheet card-front" aria-label="Business card front">
    <div class="card-band"></div>
    <div class="brand">
      <span class="brand-dot"></span>
      <div>
        <div class="brand-name">BREVIX</div>
        <div class="brand-sub">Brevix Systems Group</div>
        <div class="brand-tag">Strategic Consulting</div>
      </div>
    </div>
    <div class="card-person">
      <p>Dermot Ashby</p>
      <p class="role">Managing Director</p>
    </div>
    <div class="card-address">
      <p>27 Larch Chambers</p>
      <p>62 Pellbrook Gardens</p>
      <p>Ashmere, Hollbury. TW3 5RJ</p>
      <p><span class="label">Phone:</span> 01632 960 418 <span class="label">| Cell:</span> 07700 900 612</p>
      <p><span class="label">Email:</span> dermot.ashby@brevix.com | www.brevix.com</p>
    </div>
    <div class="card-faint"></div>
  </section>

  <section class="sheet card-logo card-blue" aria-label="Business card back, blue">
    <div class="brand">
      <span class="brand-dot"></span>
      <div>
        <div class="brand-name">BREVIX</div>
        <div class="brand-sub">Brevix Systems Group</div>
        <div class="brand-tag">Strategic Consulting</div>
      </div>
    </div>
  </section>

  <section class="sheet card-logo card-black" aria-label="Business card back, black">
    <div class="brand">
      <span class="brand-dot"></span>
      <div>
        <div class="brand-name">BREVIX</div>
        <div class="brand-sub">Brevix Systems Group</div>
        <div class="brand-tag">Strategic Consulting</div>
      </div>
    </div>
  </section>

  <section class="sheet envelope" aria-label="DL envelope">
    <svg class="flap" width="607" height="140" viewBox="0 0 607 140" aria-hidden="true">
      <defs>
        <linearGradient id="flapFill" x1="0" y1="0" x2="1" y2="0">
          <stop offset="0" stop-color="#123a8a"/>
          <stop offset=".5" stop-color="#3f8fdc"/>
          <stop offset="1" stop-color="#123a8a"/>
        </linearGradient>
      </defs>
      <path d="M0 0H607V58Q540 76 303 128Q66 76 0 58Z" fill="url(#flapFill)"/>
    </svg>
    <span class="flap-mark"></span>
    <div class="brand">
      <span class="brand-dot"></span>
      <div>
        <div class="brand-name">BREVIX</div>
        <div class="brand-sub">Brevix Systems Group</div>
        <div class="brand-tag">Strategic Consulting</div>
      </div>
    </div>
    <div class="env-address">
      <p>27 Larch Chambers</p>
      <p>62 Pellbrook Gardens</p>
      <p>Ashmere, Hollbury. TW3 5RJ</p>
    </div>
    <div class="env-faint"></div>
  </section>

</main>
</body>
</html>
```